Letterhead & Email Signature Design

Kindly assist redesign this letterhead as well as the Email signature. I have uploaded the current designs that needs some new look

```html
<!DOCTYPE html>
<html lang="en">
<head>
<meta charset="utf-8">
<title>Moloi Dube Inc – Letterhead &amp; Email Signature</title>
<link href="https://fonts.googleapis.com/css2?family=Roboto+Condensed:wght@400&family=Work+Sans:wght@400;500&display=swap" rel="stylesheet">
<style>
  :root {
    --backdrop: #ababab;
    --paper: #ffffff;
    --ink: #111111;
    --mark-grey: #666666;
    --soft-ink: #666666;
    --rule: #111111;
  }
  * { margin: 0; padding: 0; box-sizing: border-box; }
  html, body { width: 991px; height: 1200px; overflow: hidden; }
  body { background: var(--backdrop); position: relative; font-family: "Roboto Condensed", "Arial Narrow", sans-serif; color: var(--ink); }

  .letterhead { position: absolute; left: 199px; top: 76px; width: 593px; height: 839px; background: var(--paper); }
  .letterhead .brand-dot { position: absolute; left: 75px; top: 17px; width: 87px; height: 87px; border-radius: 50%; background: var(--mark-grey); }
  .letterhead .brand-name { position: absolute; left: 170px; top: 51px; font-size: 15px; color: var(--mark-grey); white-space: nowrap; }
  .letterhead .practice { position: absolute; left: 0; width: 238px; top: 113px; text-align: center; font-size: 9.6px; line-height: 13px; letter-spacing: 0.1px; }

  .footer-rule { position: absolute; left: 16px; right: 16px; top: 767px; height: 2px; background: var(--rule); }
  .footer-line { position: absolute; font-size: 9.6px; line-height: 12px; white-space: nowrap; display: flex; align-items: center; gap: 5px; }
  .footer-line svg { flex: none; }
  .footer-divider { position: absolute; left: 358px; top: 780px; width: 1px; height: 44px; background: var(--rule); }
  .directors { position: absolute; left: 372px; top: 779px; font-size: 9.4px; line-height: 11.9px; white-space: nowrap; }

  .signature { position: absolute; left: 319px; top: 972px; width: 353px; height: 145px; background: var(--paper); font-family: "Work Sans", Arial, sans-serif; color: var(--soft-ink); }
  .signature .brand-dot { position: absolute; left: 25px; top: 20px; width: 82px; height: 82px; border-radius: 50%; background: var(--mark-grey); }
  .signature .brand-name { position: absolute; left: 0; width: 132px; top: 105px; text-align: center; font-size: 8.4px; font-weight: 500; }
  .signature .est { position: absolute; left: 0; width: 132px; top: 116px; text-align: center; font-size: 7.2px; }
  .signature .divider { position: absolute; left: 123px; top: 19px; width: 1.5px; height: 106px; background: var(--soft-ink); }
  .signature .person { position: absolute; left: 138px; top: 19px; font-size: 12.2px; font-weight: 500; letter-spacing: 0.2px; }
  .signature .role { position: absolute; left: 138px; top: 33px; font-size: 10px; }
  .contact-row { position: absolute; left: 138px; display: flex; align-items: flex-start; gap: 7px; font-size: 8.4px; line-height: 11.5px; }
  .contact-row svg { flex: none; margin-top: 1px; }
</style>
</head>
<body>

<section class="letterhead">
  <div class="brand-dot"></div>
  <div class="brand-name">Moloi Dube Inc</div>
  <div class="practice">ATTORNEYS • CONVEYANCERS • NOTARIES<br>Reg. No.: 2009/004318/21</div>

  <div class="footer-rule"></div>

  <div class="footer-line" style="left:20px; top:781px;">
    <svg width="8" height="11" viewBox="0 0 8 11"><path d="M4 0a4 4 0 0 0-4 4c0 3 4 7 4 7s4-4 4-7a4 4 0 0 0-4-4z" fill="#444"/><circle cx="4" cy="4" r="1.5" fill="#fff"/></svg>
    <span>The Acacia Business Park &nbsp;• Ground Floor, Building A 214</span>
  </div>
  <div class="footer-line" style="left:32px; top:797px;"><span>Elmstead Road • Lynnwood Ridge 0040</span></div>
  <div class="footer-line" style="left:16px; top:813px; font-size:10.2px;">
    <svg width="12" height="8" viewBox="0 0 12 8"><rect width="12" height="8" fill="#333"/><path d="M0 0l6 4.5L12 0" stroke="#fff" stroke-width="1" fill="none"/></svg>
    <span>info@moloidube.co.za</span>
    <svg style="margin-left:8px" width="11" height="11" viewBox="0 0 11 11"><rect x="0" y="2" width="4" height="9" fill="#444"/><rect x="4.5" y="0" width="6.5" height="11" rx="1" fill="none" stroke="#444" stroke-width="1.2"/></svg>
    <span>012 555 0147</span>
    <svg style="margin-left:12px" width="12" height="9" viewBox="0 0 12 9"><path d="M0 3c0-2 12-2 12 0v1H9V3H3v1H0z" fill="#444"/><rect x="2" y="4" width="8" height="5" rx="1" fill="#444"/></svg>
    <span>012 555 0186</span>
  </div>

  <div class="footer-divider"></div>
  <div class="directors">Directors:<br>L T Moloi B. PROC LLB (Hons) | P Dube (LLB)<br>Consultant:<br>TN Dube</div>
</section>

<section class="signature">
  <div class="brand-dot"></div>
  <div class="brand-name">Moloi Dube Inc</div>
  <div class="est">Est. 2009</div>
  <div class="divider"></div>
  <div class="person">LERATO MOLOI</div>
  <div class="role">Director</div>

  <div class="contact-row" style="top:54px;">
    <svg width="9" height="12" viewBox="0 0 8 11" style="margin-left:2px"><path d="M4 0a4 4 0 0 0-4 4c0 3 4 7 4 7s4-4 4-7a4 4 0 0 0-4-4z" fill="#666"/><circle cx="4" cy="4" r="1.5" fill="#fff"/></svg>
    <span style="margin-left:2px">214 Elmstead Road, The Acacia Business Park,<br>Ground Floor, Building A,</span>
  </div>
  <div class="contact-row" style="top:82px;">
    <svg width="12" height="9" viewBox="0 0 12 9"><path d="M0 3c0-2 12-2 12 0v1H9V3H3v1H0z" fill="#666"/><rect x="2" y="4" width="8" height="5" rx="1" fill="#666"/></svg>
    <span style="margin-left:1px">+27 12 555 0186</span>
  </div>
  <div class="contact-row" style="top:97px;">
    <svg width="12" height="8" viewBox="0 0 12 8"><rect width="12" height="8" fill="#666"/><path d="M0 0l6 4.5L12 0" stroke="#fff" stroke-width="1" fill="none"/></svg>
    <span style="margin-left:1px">lerato@moloidube.co.za</span>
  </div>
  <div class="contact-row" style="top:113px;">
    <svg width="12" height="12" viewBox="0 0 12 12" fill="none" stroke="#666" stroke-width="0.9"><circle cx="6" cy="6" r="5.3"/><ellipse cx="6" cy="6" rx="2.4" ry="5.3"/><path d="M0.7 6h10.6M1.6 3.3h8.8M1.6 8.7h8.8"/></svg>
    <span style="margin-left:1px">www.moloidubeinc.co.za</span>
  </div>
</section>

</body>
</html>
```